Design a "Membership Directory" in word

I work for an oil and gas society. I am creating a digital directory of all our members in word (to be exported to .pdf). The content is created. All I want is someone to make it prettier.

Attached is the current template and photos.

to do:

Make front look nicer
Add the photos to the table of contents
Create headers and footers on the two different sections (members section / company section)

- Please deliver in .docx format
- Please keep orientation vertical. It won't be printed.

update:

This is very conservative group. It really just needs to look professional. A great deal of design is not required. Sometimes less is more.

```html
<!DOCTYPE html>
<html lang="en">
<head>
<meta charset="utf-8">
<title>Membership Directory 2014</title>
<link rel="stylesheet" href="https://fonts.googleapis.com/css2?family=Open+Sans:wght@400;600;700&display=swap">
<style>
  :root {
    --stage: #8e8e8e;
    --paper: #ffffff;
    --gold: #8a6d3b;
    --gold-light: #b49a63;
    --ink: #4a4a4a;
    --ink-soft: #8a8a8a;
    --panel: #e7e7e7;
    --photo-a: #7a2a26;
    --photo-b: #3c3a3d;
    --photo-c: #b7a58b;
  }
  * { box-sizing: border-box; margin: 0; padding: 0; }
  html, body { width: 1200px; height: 795px; overflow: hidden; }
  body {
    position: relative;
    background: var(--stage);
    font-family: "Open Sans", sans-serif;
    color: var(--ink);
  }
  .page {
    position: absolute;
    background: var(--paper);
    width: 263px;
    height: 340px;
    overflow: hidden;
    box-shadow: 0 6px 16px rgba(0,0,0,.25);
  }
  .photo {
    background: linear-gradient(135deg, var(--photo-a), var(--photo-b) 60%, var(--photo-c));
  }
  .photo.warm { background: linear-gradient(135deg, var(--photo-c), var(--photo-a) 55%, var(--photo-b)); }
  .photo.dark { background: linear-gradient(160deg, var(--photo-b), var(--photo-c)); }

  .brand { position: absolute; display: flex; align-items: center; gap: 4px; }
  .brand-mark { width: 16px; height: 16px; border-radius: 50%; border: 1.5px solid var(--gold); }
  .brand-name { font-size: 5px; font-weight: 700; letter-spacing: .4px; text-transform: uppercase; color: var(--gold); }

  /* Cover */
  .cover { left: 168px; top: 28px; }
  .cover .brand { left: 0; right: 0; top: 22px; flex-direction: column; gap: 4px; }
  .cover .brand-mark { width: 26px; height: 26px; border-width: 2px; }
  .cover-photos { position: absolute; left: 46px; right: 0; top: 76px; height: 48px; display: flex; gap: 2px; }
  .cover-photos .photo { flex: 1; }
  .cover-band {
    position: absolute; left: 46px; right: 0; top: 126px; height: 18px;
    background: var(--gold); display: flex; align-items: center; justify-content: flex-end; gap: 6px;
    padding-right: 4px;
  }
  .cover-title { color: #fff; font-size: 9px; font-weight: 600; }
  .year-box { background: #fff; color: var(--gold); font-size: 8px; font-weight: 700; padding: 1px 4px; }
  .cover-address { position: absolute; left: 120px; top: 196px; font-size: 4.5px; line-height: 1.6; color: var(--ink-soft); }

  /* Spread */
  .spread-left { left: 637px; top: 28px; background: #f4f4f4; }
  .spread-right { left: 900px; top: 28px; box-shadow: 6px 6px 16px rgba(0,0,0,.25); }
  .spread-left .brand { left: 14px; top: 16px; }
  .spread-left .brand-mark { width: 24px; height: 24px; }
  .toc-title { position: absolute; left: 46px; top: 16px; font-size: 10px; font-weight: 700; line-height: 1.2; color: var(--ink); }
  .hero { position: absolute; left: 14px; right: 14px; top: 50px; height: 76px; }
  .toc-rule {
    position: absolute; left: 14px; right: 14px; top: 130px; height: 10px;
    border-top: 2px solid var(--gold);
    font-size: 5px; font-weight: 700; color: var(--gold); text-align: right; padding-top: 2px; letter-spacing: .5px;
  }
  .toc-panel { position: absolute; left: 14px; right: 14px; top: 148px; bottom: 40px; background: var(--panel); padding: 10px; }
  .toc-entry { display: flex; justify-content: space-between; font-size: 5.5px; line-height: 1.7; color: var(--ink); }
  .toc-photos { display: flex; gap: 8px; margin-top: 12px; }
  .toc-photos .photo { flex: 1; height: 36px; border: 2px solid #fff; }

  .section-head {
    position: absolute; left: 14px; right: 14px; top: 14px; height: 14px;
    display: flex; align-items: center; gap: 6px;
  }
  .section-head .brand { position: static; }
  .section-bar {
    flex: 1; height: 12px; background: var(--gold); color: #fff;
    font-size: 6.5px; font-weight: 600; padding: 1px 6px;
  }
  .columns { position: absolute; left: 14px; right: 14px; top: 40px; display: grid; grid-template-columns: repeat(3, 1fr); gap: 8px; }
  .entry { margin-bottom: 7px; font-size: 4.8px; line-height: 1.4; }
  .entry b { display: block; color: var(--gold); font-weight: 700; }
  .entry span { color: var(--ink-soft); }

  /* Caption */
  .caption {
    position: absolute; left: 0; top: 397px; width: 600px; height: 398px;
    display: flex; align-items: center; justify-content: center;
    font-size: 30px; color: #fff; font-weight: 400;
  }

  /* Directory page */
  .list-page { left: 768px; top: 428px; }
  .list-page .brand { left: 14px; top: 16px; }
  .list-photos { position: absolute; left: 44px; right: 14px; top: 12px; height: 26px; display: flex; gap: 3px; }
  .list-photos .photo { flex: 1; }
  .list-page .columns { top: 50px; }
  .list-footer {
    position: absolute; left: 14px; right: 0; bottom: 16px; height: 14px;
    background: var(--gold-light); display: flex; align-items: center; justify-content: flex-end; gap: 5px; padding-right: 4px;
  }
  .list-footer .cover-title { font-size: 7px; }
  .list-footer .year-box { font-size: 6.5px; }
</style>
</head>
<body>

<!-- Cover -->
<section class="page cover">
  <div class="brand">
    <div class="brand-mark"></div>
    <div class="brand-name">Gulf Basin Geological Society</div>
  </div>
  <div class="cover-photos">
    <div class="photo" role="img" aria-label="Members at a society dinner"></div>
    <div class="photo warm" role="img" aria-label="Award presentation on stage"></div>
    <div class="photo dark" role="img" aria-label="Members talking at a reception"></div>
    <div class="photo" role="img" aria-label="Guests at the annual event"></div>
  </div>
  <div class="cover-band">
    <span class="cover-title">Membership Directory</span>
    <span class="year-box">2014</span>
  </div>
  <p class="cover-address">1200 Basin Street, Suite 400<br>Westport, TX 77000 · 555-0142</p>
</section>

<!-- Spread: table of contents -->
<section class="page spread-left">
  <div class="brand"><div class="brand-mark"></div></div>
  <h1 class="toc-title">2014 GBGS<br>Membership Directory</h1>
  <div class="photo warm hero" role="img" aria-label="Two members at an event"></div>
  <div class="toc-rule">TABLE OF CONTENTS</div>
  <div class="toc-panel">
    <div class="toc-entry"><span>Members by Name</span><span>03</span></div>
    <div class="toc-entry"><span>Members by Company Affiliation</span><span>18</span></div>
    <div class="toc-photos">
      <div class="photo" role="img" aria-label="Members at a podium"></div>
      <div class="photo dark" role="img" aria-label="Members at a luncheon"></div>
      <div class="photo warm" role="img" aria-label="Group at a field trip"></div>
    </div>
  </div>
</section>

<!-- Spread: members by name -->
<section class="page spread-right">
  <div class="section-head">
    <div class="brand"><div class="brand-mark"></div></div>
    <div class="section-bar">Members by Name</div>
  </div>
  <div class="columns">
    <div>
      <div class="entry"><b>Abbott, Grace</b><span>Delta Energy</span></div>
      <div class="entry"><b>Acosta, Luis</b><span>Ridgeline Oil</span></div>
      <div class="entry"><b>Adams, Peter</b><span>Harbor Rock Co.</span></div>
      <div class="entry"><b>Aiken, Laura</b><span>Summit Gas</span></div>
      <div class="entry"><b>Alder, Mark</b><span>Crestline E&amp;P</span></div>
      <div class="entry"><b>Allen, Ruth</b><span>Bayou Resources</span></div>
    </div>
    <div>
      <div class="entry"><b>Alvarez, Sam</b><span>Pinegate Oil</span></div>
      <div class="entry"><b>Ames, Carol</b><span>Northfork Gas</span></div>
      <div class="entry"><b>Andrews, Neil</b><span>Delta Energy</span></div>
      <div class="entry"><b>Archer, Jane</b><span>Ridgeline Oil</span></div>
      <div class="entry"><b>Arnold, Tom</b><span>Summit Gas</span></div>
      <div class="entry"><b>Ash, Helen</b><span>Bayou Resources</span></div>
    </div>
    <div>
      <div class="entry"><b>Atkins, Paul</b><span>Harbor Rock Co.</span></div>
      <div class="entry"><b>Austin, Kate</b><span>Crestline E&amp;P</span></div>
      <div class="entry"><b>Avery, Dan</b><span>Pinegate Oil</span></div>
      <div class="entry"><b>Ayers, Mia</b><span>Northfork Gas</span></div>
      <div class="entry"><b>Baker, Joel</b><span>Delta Energy</span></div>
      <div class="entry"><b>Baird, Anne</b><span>Summit Gas</span></div>
    </div>
  </div>
</section>

<div class="caption">"Membership Directory"</div>

<!-- Directory page -->
<section class="page list-page">
  <div class="brand"><div class="brand-mark"></div></div>
  <div class="list-photos">
    <div class="photo" role="img" aria-label="Members at a society dinner"></div>
    <div class="photo dark" role="img" aria-label="Speaker addressing members"></div>
    <div class="photo warm" role="img" aria-label="Members at a reception"></div>
  </div>
  <div class="columns">
    <div>
      <div class="entry"><b>Ball, Owen</b><span>Ridgeline Oil</span></div>
      <div class="entry"><b>Banks, Lisa</b><span>Delta Energy</span></div>
      <div class="entry"><b>Barker, Hugh</b><span>Summit Gas</span></div>
      <div class="entry"><b>Barnes, Ella</b><span>Bayou Resources</span></div>
      <div class="entry"><b>Bates, Ross</b><span>Pinegate Oil</span></div>
      <div class="entry"><b>Bell, Nora</b><span>Northfork Gas</span></div>
    </div>
    <div>
      <div class="entry"><b>Bennett, Ian</b><span>Harbor Rock Co.</span></div>
      <div class="entry"><b>Berry, Joan</b><span>Crestline E&amp;P</span></div>
      <div class="entry"><b>Black, Carl</b><span>Delta Energy</span></div>
      <div class="entry"><b>Blair, Dana</b><span>Summit Gas</span></div>
      <div class="entry"><b>Bond, Eric</b><span>Ridgeline Oil</span></div>
      <div class="entry"><b>Boyd, Lena</b><span>Bayou Resources</span></div>
    </div>
    <div>
      <div class="entry"><b>Bryant, Cole</b><span>Pinegate Oil</span></div>
      <div class="entry"><b>Burke, Tess</b><span>Northfork Gas</span></div>
      <div class="entry"><b>Burns, Adam</b><span>Harbor Rock Co.</span></div>
      <div class="entry"><b>Butler, Amy</b><span>Crestline E&amp;P</span></div>
      <div class="entry"><b>Byrd, Glen</b><span>Delta Energy</span></div>
      <div class="entry"><b>Cain, Rosa</b><span>Summit Gas</span></div>
    </div>
  </div>
  <div class="list-footer">
    <span class="cover-title">Membership Directory</span>
    <span class="year-box">2014</span>
  </div>
</section>

</body>
</html>
```